Velmora Systems Business Card Design

We need a new design for our IT Security and Management consulting business. we're based out of NY so NYC elements can (and should) be incorporated. We focus on financial services companies but aren't exclusive, so elements with financial services can be included as well. I'm looking for something clean and modern, a bit bold but nothing crazy and not busy.

Target Market(s)

Financial Services and Small Business

Industry/Entity Type

It Company

Contact Information for Business Card

Dorin Kaltsenberg
President/CTO
555-555-0143
dk@velmorasys.example
718 Bramblecourt Avenue
Suite 305-#14
Ashby Ridge, NY 07921
www.velmorasys.example

Font styles to use
Serif
Sans Serif

Colors
f37122
ec1f27
3176b5

Requirements
Must have
• "white" space on one side. (doesn't actually have to be white). we plan to use Pexa.example which will have an orange middle edge between front and back. (see attached example). Logo attached.
Nice to have
• new york city scape

```html
<!DOCTYPE html>
<html lang="en">
<head>
<meta charset="utf-8">
<title>Velmora Systems Business Card</title>
<link rel="stylesheet" href="https://fonts.googleapis.com/css2?family=Work+Sans:wght@300;400;600;700&display=swap">
<style>
  :root {
    --backdrop: #d35a1f;
    --card-white: #f2f2f2;
    --brand-orange: #f37122;
    --brand-red: #ec1f27;
    --brand-blue: #3176b5;
    --ink: #555555;
    --ink-strong: #3c3c3c;
    --city-light: #e6e6e6;
    --city-mid: #a9a9a9;
    --city-dark: #6f6f6f;
    --white: #ffffff;
  }
  * { box-sizing: border-box; margin: 0; padding: 0; }
  html, body {
    width: 1200px;
    height: 873px;
    overflow: hidden;
  }
  body {
    background: var(--backdrop);
    font-family: "Work Sans", Arial, sans-serif;
    color: var(--ink);
    position: relative;
  }
  .card {
    position: absolute;
    top: 294px;
    width: 500px;
    height: 286px;
    border-bottom: 6px solid var(--brand-orange);
    box-shadow: 0 10px 24px rgba(80, 25, 0, 0.35);
    overflow: hidden;
  }
  .card--front {
    left: 70px;
    background: var(--card-white);
    padding: 30px 34px;
  }
  .card--back {
    left: 630px;
  }

  .brand {
    display: flex;
    align-items: center;
    gap: 10px;
  }
  .brand__dot {
    width: 22px;
    height: 22px;
    border-radius: 50%;
    background: var(--brand-red);
  }
  .brand__name {
    font-weight: 700;
    font-size: 26px;
    color: var(--brand-blue);
    letter-spacing: 0.2px;
  }

  .person { margin-top: 18px; }
  .person__name {
    font-weight: 600;
    font-size: 15px;
    color: var(--ink-strong);
  }
  .person__title {
    font-weight: 300;
    font-size: 13px;
    margin-top: 2px;
  }

  .details {
    position: absolute;
    left: 34px;
    right: 34px;
    bottom: 30px;
    display: flex;
    align-items: flex-end;
  }
  .contact {
    list-style: none;
    font-weight: 300;
    font-size: 13px;
    line-height: 1.55;
  }
  .contact__label {
    display: inline-block;
    width: 14px;
    font-weight: 600;
    color: var(--ink-strong);
  }
  .contact__web { color: var(--brand-orange); }
  .divider {
    width: 2px;
    height: 62px;
    background: var(--brand-orange);
    margin: 0 26px 2px 30px;
  }
  .address {
    font-style: normal;
    font-weight: 300;
    font-size: 14px;
    line-height: 1.5;
  }

  .skyline {
    position: absolute;
    inset: 0;
    background: linear-gradient(180deg, var(--city-light) 0%, var(--city-mid) 45%, var(--city-dark) 100%);
  }
  .back-mark {
    position: absolute;
    inset: 0;
    display: flex;
    align-items: center;
    justify-content: center;
    gap: 12px;
  }
  .back-mark__ring {
    width: 26px;
    height: 26px;
    border-radius: 50%;
    border: 4px solid var(--white);
  }
  .back-mark__name {
    font-weight: 700;
    font-size: 26px;
    color: var(--white);
  }
</style>
</head>
<body>
  <section class="card card--front" aria-label="Business card front">
    <div class="brand">
      <span class="brand__dot"></span>
      <span class="brand__name">Velmora Systems</span>
    </div>
    <div class="person">
      <p class="person__name">Dorin Kaltsenberg</p>
      <p class="person__title">President/CTO</p>
    </div>
    <div class="details">
      <ul class="contact">
        <li><span class="contact__label">t</span>555-555-0143</li>
        <li><span class="contact__label">e</span>dk@velmorasys.example</li>
        <li class="contact__web">www.velmorasys.example</li>
      </ul>
      <span class="divider"></span>
      <address class="address">
        718 Bramblecourt Avenue<br>
        Suite 305-#14<br>
        Ashby Ridge, NY 07921
      </address>
    </div>
  </section>

  <section class="card card--back" aria-label="Business card back">
    <div class="skyline" role="img" aria-label="Black and white aerial photograph of a city skyline"></div>
    <div class="back-mark">
      <span class="back-mark__ring"></span>
      <span class="back-mark__name">Velmora Systems</span>
    </div>
  </section>
</body>
</html>
```